I have a small construction company that is growing. I specialize in commercial concrete and custom

I want a site that shows what we do. We specialize in custom deck design and builds. Custom home builds. Commercial concrete . project management

Target Market(s)

Commercial construction companies and custom home builders

Industry/Entity Type

Construction

Number of Pages Required

1 page

Font styles to use
Serif

Colors

Designer to choose colors to be used in the design.

Requirements
Must have
• Pictures and videos of project that we have completed or are in progress

```html
<!DOCTYPE html>
<html lang="en">
<head>
<meta charset="utf-8">
<title>Construction Company</title>
<link href="https://fonts.googleapis.com/css2?family=Montserrat:wght@700;800&family=Roboto:wght@400;500;700&display=swap" rel="stylesheet">
<style>
:root{
  --yellow:#fdc010;
  --black:#000;
  --ink:#111;
  --white:#fff;
  --grey:#2b2b2b;
  --muted:#bdbdbd;
}
*{box-sizing:border-box;margin:0;padding:0}
html,body{width:1200px;height:3879px;overflow:hidden}
body{font-family:'Roboto',Arial,sans-serif;color:var(--white);background:var(--black);position:relative}
section,header,footer{position:absolute;left:0;width:1200px;overflow:hidden}
.abs{position:absolute}
.center{left:0;width:1200px;text-align:center}
.section-title{font-weight:500;font-size:31px;letter-spacing:.5px}
.btn{position:absolute;display:flex;align-items:center;justify-content:center;border-radius:14px;font-size:12px;font-weight:500;height:28px}
.btn-yellow{background:var(--yellow);color:var(--ink)}
.btn-white{background:var(--white);color:var(--ink)}
.btn-dark{background:var(--grey);color:var(--white)}
.arrows{position:absolute;display:flex;gap:6px}
.arrows span{width:16px;height:16px;border-radius:50%;display:flex;align-items:center;justify-content:center}

/* header */
.site-header{top:0;height:98px;background:var(--black)}
.logo{font-family:'Montserrat',Arial,sans-serif;font-weight:800;color:var(--yellow);font-size:34px;letter-spacing:1px}
.main-nav{position:absolute;left:556px;top:40px;display:flex;gap:24px;font-size:14px}
.main-nav a{color:var(--white);text-decoration:none;position:relative}
.main-nav a.active::after{content:"";position:absolute;left:4px;right:4px;top:48px;height:4px;background:var(--yellow)}

/* hero */
.hero{top:98px;height:587px;background:linear-gradient(180deg,#8e9aa8 0%,#b7a6a6 30%,#4e5a66 55%,#5d5b5a 75%,#2e2b29 100%)}
.hero-title{top:272px;font-family:'Montserrat',Arial,sans-serif;font-weight:800;font-size:40px;color:var(--yellow);letter-spacing:1px}

/* services */
.services{top:685px;height:292px;background:var(--black)}
.service{position:absolute;top:118px;width:200px;text-align:center;font-size:13px;line-height:16px}
.service .icon{width:72px;height:72px;border-radius:50%;background:var(--yellow);margin:0 auto 12px;display:flex;align-items:center;justify-content:center}
.service.dim .icon{background:#2f2f2f}
.service.dim p{color:var(--yellow)}

/* about */
.about{top:977px;height:347px;background:var(--yellow);color:var(--ink)}
.about h2{left:124px;top:73px;font-size:31px;font-weight:500}
.about .rule{left:300px;top:92px;width:295px;height:2px;background:var(--ink)}
.about p{left:124px;top:146px;width:490px;font-size:13px;line-height:17px}
.video{left:646px;top:50px;width:412px;height:245px;border:7px solid var(--white);background:linear-gradient(135deg,#9a9a9a,#5e5e5e 50%,#8a8a8a)}
.play{left:185px;top:91px;width:50px;height:50px;border-radius:50%;background:#e0242b;display:flex;align-items:center;justify-content:center}

/* projects */
.projects{top:1324px;height:502px;background:var(--black)}
.project{position:absolute;top:137px;width:302px;height:246px}
.project-info{background:rgba(253,192,16,.9);color:var(--ink)}
.project-info h3{position:absolute;left:18px;top:20px;font-size:25px;font-weight:500}
.project-info span{position:absolute;left:18px;top:52px;font-size:14px}

/* testimonials */
.testimonials{top:1826px;height:403px;background:var(--yellow);color:var(--ink)}
.t-card{position:absolute;top:101px;width:340px;height:181px;padding:18px 0 0 90px}
.t-card.dark{background:var(--black);color:var(--white)}
.t-card.light{background:var(--white);color:var(--ink)}
.t-card .quote{position:absolute;left:60px;top:10px;font-family:Georgia,serif;font-size:46px;font-weight:700;line-height:46px}
.t-card h4{font-size:20px;font-weight:500}
.t-card .role{font-size:13px}
.t-card .stars{color:var(--yellow);font-size:12px;letter-spacing:2px}
.t-card p{font-size:12px;line-height:15px;margin-top:12px;width:200px}
.t-card .more{position:absolute;right:26px;bottom:18px;font-size:13px}
.avatar{position:absolute;width:124px;height:124px;border-radius:50%;border:6px solid var(--yellow);background:linear-gradient(160deg,#c5b8a6,#7e7168)}
.avatar.w{border-color:var(--yellow)}

/* blogs */
.blogs{top:2229px;height:636px;background:var(--black)}
.post{position:absolute;top:114px;width:300px;height:419px;background:var(--white);color:var(--ink)}
.post.featured{background:var(--yellow)}
.post .thumb{height:204px}
.date{position:absolute;left:117px;top:171px;width:66px;height:66px;border-radius:50%;background:var(--white);border:4px solid var(--yellow);text-align:center;padding-top:7px}
.post.featured .date{border-color:var(--white)}
.date b{display:block;font-size:22px;font-weight:500;line-height:24px}
.date small{font-size:8px}
.post h3{position:absolute;top:262px;width:300px;text-align:center;font-size:31px;font-weight:400}
.post p{position:absolute;top:302px;left:30px;width:240px;text-align:center;font-size:12px;line-height:15px}
.post .meta{position:absolute;top:381px;left:20px;right:20px;display:flex;justify-content:space-between;font-size:12px}

/* newsletter */
.newsletter{top:2865px;height:264px;background:var(--yellow);color:var(--ink)}
.newsletter h2{top:64px}
.newsletter .underline{left:570px;top:106px;width:60px;height:3px;background:var(--ink)}
.subscribe{left:349px;top:135px;width:499px;height:46px;border-radius:23px;background:var(--black);display:flex;align-items:center;padding:0 4px 0 4px}
.subscribe .field{flex:1;height:38px;border-radius:19px;background:var(--yellow);margin-right:14px;border:none;padding-left:20px;font-size:12px;display:flex;align-items:center}

/* clients */
.clients{top:3129px;height:316px;background:var(--black)}
.client{position:absolute;top:127px;width:140px;height:106px;background:var(--white);color:var(--ink);display:flex;align-items:center;justify-content:center;font-size:17px;font-weight:700;gap:6px}
.client i{width:10px;height:10px;background:#1f4e8c;display:inline-block}

/* footer */
.site-footer{top:3445px;height:434px;background:linear-gradient(180deg,#3a3633 0%,#2a2725 60%,#1c1a19 100%)}
.site-footer h4{font-size:22px;font-weight:700}
.site-footer .small{font-size:15px;line-height:18px}
.divider{width:3px;height:58px;background:var(--white)}
.f-rule{left:124px;top:145px;width:958px;height:1px;background:var(--white)}
.f-logo{font-family:'Montserrat',Arial,sans-serif;color:var(--yellow);font-weight:700;font-size:34px}
.quick a{display:block;color:var(--white);text-decoration:none;font-size:12px;line-height:22px}
.f-sub{left:789px;top:215px;width:292px;height:24px;border-radius:12px;background:var(--white);color:var(--ink);font-size:10px;display:flex;align-items:center;padding-left:14px}
.f-sub span{margin-left:auto;width:40px;height:24px;border-radius:12px;background:var(--black);display:flex;align-items:center;justify-content:center}
.social{left:970px;top:380px;display:flex;gap:8px}
.social span{width:30px;height:30px;border-radius:50%;border:2px solid var(--white);display:block}
</style>
</head>
<body>

<header class="site-header">
  <div class="abs logo" style="left:124px;top:28px">YOUR LOGO</div>
  <nav class="main-nav">
    <a class="active" href="#">Home</a><a href="#">About us</a><a href="#">Services</a><a href="#">Projects</a><a href="#">Blogs</a><a href="#">Contact us</a>
  </nav>
  <div class="btn btn-yellow" style="left:983px;top:36px;width:100px;height:26px">Get a Quote</div>
</header>

<section class="hero" role="img" aria-label="City skyline at dusk seen from a curved waterfront boardwalk">
  <h1 class="abs center hero-title">WE INNOVATE</h1>
  <div class="btn btn-yellow" style="left:532px;top:354px;width:136px">Read More</div>
</section>

<section class="services">
  <h2 class="abs center section-title" style="top:43px">WHAT WE DO</h2>
  <div class="service dim" style="left:120px">
    <div class="icon"><svg width="36" height="36" viewBox="0 0 36 36" fill="none" stroke="#fdc010" stroke-width="2"><rect x="5" y="5" width="26" height="26"/><path d="M9 25l7-8 5 5 3-3 4 6z"/><circle cx="24" cy="12" r="2"/></svg></div>
    <p>Custom Deck Design<br>And Builds</p>
  </div>
  <div class="service" style="left:378px">
    <div class="icon"><svg width="38" height="38" viewBox="0 0 38 38" fill="none" stroke="#111" stroke-width="2.2"><path d="M5 19L19 7l14 12"/><path d="M9 16v15h20V16"/><rect x="16" y="22" width="6" height="9"/></svg></div>
    <p>Custom Home<br>Builds</p>
  </div>
  <div class="service" style="left:627px">
    <div class="icon"><svg width="38" height="38" viewBox="0 0 38 38" fill="none" stroke="#111" stroke-width="2.2"><path d="M7 15c6-8 18-8 24 0l-12 6z"/><path d="M19 21v12"/><path d="M14 33h10"/></svg></div>
    <p>Commercial<br>Concrete</p>
  </div>
  <div class="service" style="left:875px">
    <div class="icon"><svg width="36" height="36" viewBox="0 0 36 36" fill="none" stroke="#111" stroke-width="2.2"><rect x="8" y="7" width="20" height="24" rx="2"/><path d="M14 5h8v5h-8z"/><path d="M12 17h12M12 22h12M12 27h8"/></svg></div>
    <p>Project Management</p>
  </div>
</section>

<section class="about">
  <h2 class="abs">ABOUT US</h2>
  <div class="abs rule"></div>
  <p class="abs">Lorem Ipsum is simply dummy text of the printing and typesetting industry. Lorem Ipsum has been the industry's standard dummy text ever since the 1500s, when an unknown printer took a galley of type and scrambled it to make a type specimen book.</p>
  <div class="abs video" role="img" aria-label="Aerial video of a construction site in progress">
    <div class="abs play"><svg width="20" height="22" viewBox="0 0 20 22"><path d="M3 2l15 9-15 9z" fill="#fff"/></svg></div>
  </div>
</section>

<section class="projects">
  <h2 class="abs center section-title" style="top:58px">OUR PROJECTS</h2>
  <div class="arrows" style="left:1044px;top:80px">
    <span style="background:var(--yellow)"><svg width="8" height="8" viewBox="0 0 8 8"><path d="M5 1L2 4l3 3" stroke="#000" stroke-width="1.6" fill="none"/></svg></span>
    <span style="background:var(--white)"><svg width="8" height="8" viewBox="0 0 8 8"><path d="M3 1l3 3-3 3" stroke="#000" stroke-width="1.6" fill="none"/></svg></span>
  </div>
  <div class="project" style="left:122px;background:linear-gradient(135deg,#f2d36a,#c9a437)" role="img" aria-label="Modern building facade with yellow overlay">
    <div class="abs project-info" style="inset:0">
      <h3>Company Name</h3><span>Location</span>
      <svg class="abs" style="left:130px;top:108px" width="42" height="42" viewBox="0 0 42 42" fill="none" stroke="#111" stroke-width="2.5"><circle cx="17" cy="17" r="12"/><path d="M26 26l12 12M17 11v12M11 17h12"/></svg>
    </div>
  </div>
  <div class="project" style="left:453px;background:linear-gradient(160deg,#9bbcd0,#3f6e86 50%,#1f3b4e)" role="img" aria-label="Glass skyscrapers viewed from below"></div>
  <div class="project" style="left:781px;background:linear-gradient(180deg,#4a86c9 0%,#7aaad8 40%,#c9b99a 60%,#8e8574 100%)" role="img" aria-label="Multi-storey office building under blue sky"></div>
  <div class="btn btn-yellow" style="left:536px;top:425px;width:130px">View More</div>
</section>

<section class="testimonials">
  <h2 class="abs center section-title" style="top:37px">TESTIMONIALS</h2>
  <div class="arrows" style="left:1044px;top:62px">
    <span style="background:var(--black)"><svg width="8" height="8" viewBox="0 0 8 8"><path d="M5 1L2 4l3 3" stroke="#fdc010" stroke-width="1.6" fill="none"/></svg></span>
    <span style="background:var(--white)"><svg width="8" height="8" viewBox="0 0 8 8"><path d="M3 1l3 3-3 3" stroke="#000" stroke-width="1.6" fill="none"/></svg></span>
  </div>
  <div class="t-card dark" style="left:236px">
    <div class="quote">“</div>
    <h4>Daniel Reyes</h4><div class="role">Client</div><div class="stars">★★★★★</div>
    <p>Lorem Ipsum is simply dummy text of the printing and typesetting industry.</p>
    <div class="more">Read More...›</div>
  </div>
  <div class="avatar" style="left:178px;top:129px" role="img" aria-label="Portrait photo of client"></div>
  <div class="t-card light" style="left:694px">
    <div class="quote">“</div>
    <h4>Harper Quinn</h4><div class="role">Client</div><div class="stars">★★★★★</div>
    <p>Lorem Ipsum is simply dummy text of the printing and typesetting industry.</p>
    <div class="more">Read More...›</div>
  </div>
  <div class="avatar" style="left:636px;top:129px;border-color:var(--yellow)" role="img" aria-label="Portrait photo of client"></div>
  <div class="btn btn-dark" style="left:536px;top:335px;width:130px">View More</div>
</section>

<section class="blogs">
  <h2 class="abs center section-title" style="top:52px">OUR LATEST BLOGS</h2>
  <div class="arrows" style="left:1044px;top:62px">
    <span style="background:var(--yellow)"><svg width="8" height="8" viewBox="0 0 8 8"><path d="M5 1L2 4l3 3" stroke="#000" stroke-width="1.6" fill="none"/></svg></span>
    <span style="background:var(--white)"><svg width="8" height="8" viewBox="0 0 8 8"><path d="M3 1l3 3-3 3" stroke="#000" stroke-width="1.6" fill="none"/></svg></span>
  </div>
  <article class="post" style="left:124px">
    <div class="thumb" style="background:linear-gradient(180deg,#3f7fc4 0%,#79aee0 55%,#8a5a3a 75%,#5a3a26 100%)" role="img" aria-label="Crane over a brick building under construction"></div>
    <div class="date"><b>21</b><small>March 2018</small></div>
    <h3>TITLE 1</h3>
    <p>Lorem Ipsum is simply dummy text of the printing and typesetting industry.</p>
    <div class="meta"><span>Read More...›</span><span>◌ 20 ♡ 20</span></div>
  </article>
  <article class="post featured" style="left:453px">
    <div class="thumb" style="background:linear-gradient(180deg,#a9c6e4 0%,#c5d6e6 30%,#7a6450 55%,#4d4036 100%)" role="img" aria-label="Newly built two-storey family house"></div>
    <div class="date"><b>22</b><small>March 2018</small></div>
    <h3>TITLE 2</h3>
    <p>Lorem Ipsum is simply dummy text of the printing and typesetting industry.</p>
    <div class="meta"><span>Read More...›</span><span>◌ 20 ♡ 20</span></div>
  </article>
  <article class="post" style="left:778px">
    <div class="thumb" style="background:linear-gradient(180deg,#2f6fbf 0%,#6ea3d8 35%,#d9a585 60%,#b8b3a8 100%)" role="img" aria-label="Colourful apartment block with balconies"></div>
    <div class="date"><b>23</b><small>March 2018</small></div>
    <h3>TITLE 3</h3>
    <p>Lorem Ipsum is simply dummy text of the printing and typesetting industry.</p>
    <div class="meta"><span>Read More...›</span><span>◌ 20 ♡ 20</span></div>
  </article>
  <div class="btn btn-white" style="left:536px;top:573px;width:130px">View More</div>
</section>

<section class="newsletter">
  <h2 class="abs center section-title">SUBSCRIBE US TO NEWSLETTER</h2>
  <div class="abs underline"></div>
  <div class="abs subscribe">
    <div class="field">Your Email</div>
    <svg width="30" height="24" viewBox="0 0 24 24" style="margin-right:22px"><path d="M2 11L22 3l-6 18-4-7z" fill="#fdc010"/></svg>
  </div>
</section>

<section class="clients">
  <h2 class="abs center section-title" style="top:55px">OUR CLIENTS</h2>
  <div class="client" style="left:137px"><i></i>Baycrest</div>
  <div class="client" style="left:295px"><i></i>Veloran</div>
  <div class="client" style="left:453px">KTR</div>
  <div class="client" style="left:608px">Halvorsen</div>
  <div class="client" style="left:765px"><i></i>Northwall</div>
  <div class="client" style="left:923px">Stonebrook</div>
</section>

<footer class="site-footer" role="img" aria-label="Dim construction site photo behind footer content">
  <div class="abs" style="left:124px;top:42px"><h4>Call Us Now</h4><div class="small">202-555-0143</div></div>
  <div class="abs divider" style="left:383px;top:42px"></div>
  <div class="abs" style="left:517px;top:42px"><h4>Come Visit Now</h4><div class="small">48 Alder Ave. Palm Bay,<br>FL 32905</div></div>
  <div class="abs divider" style="left:815px;top:42px"></div>
  <div class="abs" style="left:882px;top:42px"><h4>Send Massage</h4><div class="small">hello@ironbeambuild.com</div></div>
  <div class="abs f-rule"></div>
  <div class="abs f-logo" style="left:124px;top:162px">YOUR LOGO</div>
  <p class="abs" style="left:124px;top:222px;width:210px;font-size:13px;line-height:17px;letter-spacing:1.5px">Lorem Ipsum is simply dummy text of the printing and typesetting industry.</p>
  <div class="abs" style="left:124px;top:310px;font-size:13px">Read More...›</div>
  <div class="abs" style="left:517px;top:162px"><h4>Quick Link</h4>
    <div class="quick" style="margin-top:6px"><a>HOME</a><a>ABOUT US</a><a>SERVICES</a><a>PROJECTS</a><a>TESTIMONIALS</a><a>BLOGS</a><a>CONTACT US</a></div>
  </div>
  <div class="abs" style="left:789px;top:162px"><h4>Subscribe Now</h4></div>
  <div class="abs" style="left:789px;top:199px;width:292px;height:2px;background:var(--white)"></div>
  <div class="abs f-sub">Your Email<span><svg width="14" height="12" viewBox="0 0 24 24"><path d="M2 11L22 3l-6 18-4-7z" fill="#fff"/></svg></span></div>
  <div class="abs" style="left:124px;top:380px;width:958px;height:1px;background:#777"></div>
  <div class="abs" style="left:124px;top:392px;font-size:13px">CopyRight © 2018 company name. All Right Reserve</div>
  <div class="abs social" style="top:388px" aria-label="Social media links"><span></span><span></span><span></span></div>
</footer>

</body>
</html>
```